Letterhead to Prospective Clients

Create a letterhead (word & canva) that I will use to send letters to prospective clients and also include the Coralwood Estate Partners Logo, My Contact Details and Interchangeable "Suburb". Use the same font and colour pallete

Maris Dulworth | "Suburb" Specialist - Redlands & Surrounds
Mobile: 0417 862 095
Email: MD@CoralwoodEstatePartners.com.au

```html
<!DOCTYPE html>
<html lang="en">
<head>
<meta charset="utf-8">
<title>Coralwood Estate Partners — Letterhead</title>
<link rel="stylesheet" href="https://fonts.googleapis.com/css2?family=Lato:wght@400;700&family=Montserrat:wght@300&display=swap">
<style>
  :root {
    --navy: #0b1a3b;
    --gold: #d6a77a;
    --paper: #ffffff;
    --backdrop: #dddce3;
  }
  * { margin: 0; padding: 0; box-sizing: border-box; }
  html, body {
    width: 1200px; height: 899px; overflow: hidden;
    background: var(--backdrop);
  }
  .canvas { position: relative; width: 1200px; height: 899px; }
  .letterhead {
    position: absolute; left: 295px; top: 20px;
    width: 610px; height: 860px;
    background: var(--paper);
    box-shadow: 0 6px 24px rgba(40, 40, 60, 0.18);
  }
  .brand {
    position: absolute; left: 45px; top: 26px; width: 246px;
    font-family: "Montserrat", sans-serif; font-weight: 300;
    color: var(--navy); text-align: center;
  }
  .brand-name { font-size: 38px; letter-spacing: 3px; line-height: 1; }
  .brand-sub { margin-top: 17px; font-size: 9px; letter-spacing: 3.4px; }
  .contact {
    position: absolute; left: 417px; top: 23px; height: 68px;
    border-left: 1.5px solid var(--navy);
    padding-left: 5px;
    font-family: "Lato", sans-serif; color: var(--navy);
  }
  .contact-name { font-size: 14px; font-weight: 700; line-height: 15px; }
  .contact-line { font-size: 10px; line-height: 13px; }
  .contact-role { margin-top: 2px; }
  .contact-icon { width: 8px; height: 8px; vertical-align: -1px; margin-right: 3px; fill: var(--navy); }
  .footer-band { position: absolute; left: 0; bottom: 0; width: 610px; height: 41px; display: block; }
</style>
</head>
<body>
<div class="canvas">
  <div class="letterhead">
    <div class="brand">
      <div class="brand-name">CORALWOOD</div>
      <div class="brand-sub">ESTATE PARTNERS</div>
    </div>

    <div class="contact">
      <div class="contact-name">Maris Dulworth</div>
      <div class="contact-line contact-role">Suburb Specialist</div>
      <div class="contact-line">Redlands &amp; Surrounds</div>
      <div class="contact-line">
        <svg class="contact-icon" viewBox="0 0 10 10" aria-hidden="true"><path d="M1 4 Q5 0 9 4 L8 5 L6.5 4 L6.5 3.2 Q5 2.7 3.5 3.2 L3.5 4 L2 5 Z M2.5 5.5 L7.5 5.5 L8.5 9 L1.5 9 Z"/></svg>0417 862 095
      </div>
      <div class="contact-line">
        <svg class="contact-icon" viewBox="0 0 10 10" aria-hidden="true"><path d="M0.5 2 H9.5 V8.5 H0.5 Z M0.5 2 L5 5.5 L9.5 2" stroke="#fff" stroke-width="0.8"/></svg>MD@CoralwoodEstatePartners.com.au
      </div>
    </div>

    <svg class="footer-band" viewBox="0 0 610 41" aria-hidden="true">
      <polygon points="0,0 402,0 398,4 0,4" fill="var(--gold)"/>
      <polygon points="0,6 393,6 366,41 0,41" fill="var(--navy)"/>
      <polygon points="405,0 610,0 610,41 372,41" fill="var(--gold)"/>
      <circle cx="481" cy="21" r="7" fill="#fff"/>
      <circle cx="522" cy="21" r="7" fill="#fff"/>
    </svg>
  </div>
</div>
</body>
</html>
```